Brochure Design Project

I am a Professional Painting Contractor specializing in repainting existing Commercial and Industrial building only in the Auckland N.Z market. I am looking for a tri fold brochure that will be fit into an envelope 130mm x 235mm x 6mm that I can post and also hand to perspective clients when cold calling. Please visit my web site www.brightwallcoatings.co.nz for an overview. I would like the brochure to reflect the web site. Thank you

Reason: To All designers. I am extending the deadline for 7 Days as i have been unable to spend the time to view all design submitted. Thank you all for your effort so far.

Target Market(s)

Property Managers, Building Owners, Building Tenants,

Industry/Entity Type

Building

```html
<!DOCTYPE html>
<html lang="en">
<head>
<meta charset="utf-8">
<title>Brightwall Coatings – Brochure</title>
<link href="https://fonts.googleapis.com/css2?family=Cormorant+Garamond:ital,wght@1,600&family=Open+Sans:wght@400&display=swap" rel="stylesheet">
<style>
  :root{
    --cream:#efe6d3;
    --cream-ray:#f5eee1;
    --blue:#2a6598;
    --heading:#2c6396;
    --orange:#e0731b;
    --ink:#2b2b2b;
    --white:#ffffff;
    --house-top:#4a6aa3;
    --house-mid:#34508a;
    --house-base:#6b4e38;
    --thumb-sky:#8fa9c4;
    --thumb-house:#c9c6bd;
    --thumb-ground:#3f4b35;
  }
  *{margin:0;padding:0;box-sizing:border-box}
  html,body{width:1200px;height:900px;overflow:hidden;background:var(--white)}
  .brochure{position:relative;width:1200px;height:900px;font-family:"Open Sans",Arial,sans-serif;color:var(--ink)}
  .backdrop,.hero-photo{position:absolute;left:0;top:0}
  .intro{position:absolute;left:33px;top:18px;width:385px;color:var(--orange);font-size:14.5px;line-height:19px;letter-spacing:-.25px}
  .about{position:absolute;left:651px;top:20px;width:490px}
  .about-title{font-family:"Cormorant Garamond",Georgia,serif;font-style:italic;font-weight:600;color:var(--heading);font-size:35px;line-height:40px;margin-left:3px;margin-bottom:12px}
  .about-lead{font-size:12.4px;line-height:18px;margin-bottom:10px;letter-spacing:-.15px}
  .about-note{font-size:10.5px;line-height:13.5px;margin-bottom:10px;letter-spacing:-.1px}
  .call{position:absolute;left:521px;top:332px;color:var(--white);font-size:20px;line-height:31px}
  .section-title{position:absolute;color:var(--heading);font-weight:400;line-height:1.2}
  .expertise-title{left:396px;top:474px;font-size:30px}
  .whatwedo-title{left:58px;top:605px;font-size:32px}
  .whatwedo-text{position:absolute;left:44px;top:658px;width:320px;font-size:12.5px;line-height:18px;letter-spacing:-.15px}
  .brush{position:absolute;left:38px;top:740px}
  .thumb{position:absolute;width:100px;height:76px;border:3px solid var(--white);box-shadow:0 0 3px rgba(0,0,0,.35);background:linear-gradient(to bottom,var(--thumb-sky) 0%,var(--thumb-sky) 30%,var(--thumb-house) 30%,var(--thumb-house) 78%,var(--thumb-ground) 78%)}
  .service{position:absolute;width:262px;font-size:12.4px;line-height:17.7px;letter-spacing:-.3px;text-align:justify;hyphens:auto;-webkit-hyphens:auto}
</style>
</head>
<body>
<div class="brochure">
  <svg class="backdrop" width="1200" height="900" viewBox="0 0 1200 900" aria-hidden="true">
    <rect x="18" y="0" width="1164" height="640" fill="var(--cream)"/>
    <g fill="var(--cream-ray)" opacity=".7">
      <polygon points="1182,0 1100,0 1182,120"/>
      <polygon points="1182,160 980,0 1040,0 1182,110"/>
      <polygon points="1182,210 1182,270 860,130"/>
    </g>
    <path d="M18,128 C180,95 330,80 470,120 C640,170 760,250 900,275 C1010,295 1100,300 1182,300 L1182,350 C1040,400 900,430 760,445 C600,460 420,470 280,520 C170,560 80,600 18,625 Z" fill="var(--blue)"/>
    <path d="M1182,345 C1040,395 900,425 760,440 C600,455 420,465 280,515 C170,555 80,595 18,620 L18,900 L1182,900 Z" fill="var(--cream)"/>
    <path d="M1182,356 C1040,404 900,435 760,450 C600,465 420,475 280,525 C170,565 80,605 18,630 L18,900 L1182,900 Z" fill="var(--white)"/>
  </svg>

  <svg class="hero-photo" width="1200" height="900" viewBox="0 0 1200 900" role="img" aria-label="Photograph of a two-storey blue weatherboard house with white trim and a timber deck">
    <defs>
      <linearGradient id="houseTone" x1="0" y1="0" x2="0" y2="1">
        <stop offset="0" stop-color="var(--house-top)"/>
        <stop offset=".65" stop-color="var(--house-mid)"/>
        <stop offset="1" stop-color="var(--house-base)"/>
      </linearGradient>
    </defs>
    <path d="M18,145 H385 V505 C350,510 315,515 280,525 C170,565 80,605 18,630 Z" fill="url(#houseTone)" opacity=".9"/>
  </svg>

  <p class="intro">With over 35 years experience with a multitude of clients you won't find a better team of skilled professionals to make your painting vision a reality.</p>

  <section class="about">
    <h1 class="about-title">About Brightwall Coatings</h1>
    <p class="about-lead">For the Building Owner or the Commercial Tenant we offer top quality all surface painting solutions, consultation, referrals and more, and we take pride in delivering beyond our client's expectations.</p>
    <p class="about-note">BWC are client focussed every step of the way, ensuring our communication is effective so that we understand your needs and can deliver a painting solution that meets them.</p>
    <p class="about-note">BWC ensures that whatever we do you understand where we are coming from on a technical, practical or consultative level.</p>
  </section>

  <p class="call">Or Call Martin &nbsp;Ph: 0275550148<br>for Prompt and Personal Attention.</p>

  <h2 class="section-title expertise-title">Our Expertises</h2>
  <h2 class="section-title whatwedo-title">What we do...</h2>
  <p class="whatwedo-text">B.W.C is the industry leader in Professional Painting Industry. We have 35 years of Experience and offers a Comprehensive Range of Services for Repainting</p>

  <svg class="brush" width="115" height="155" viewBox="0 0 115 155" role="img" aria-label="Illustration of a paintbrush with rainbow coloured bristles">
    <defs>
      <linearGradient id="rainbow" x1="0" y1="0" x2="1" y2="1">
        <stop offset="0" stop-color="#d62f2f"/>
        <stop offset=".35" stop-color="#f0c419"/>
        <stop offset=".65" stop-color="#3aa64c"/>
        <stop offset="1" stop-color="#6a3fa3"/>
      </linearGradient>
    </defs>
    <rect x="0" y="0" width="115" height="155" rx="20" fill="url(#rainbow)" opacity=".55"/>
  </svg>

  <div class="thumb" role="img" aria-label="Photo of a two-storey house at dusk" style="left:401px;top:529px"></div>
  <p class="service" style="left:513px;top:526px">B.W.C offers a wide range of services to All Building Owners and Occupants... Our team has expertise in all aspects of Interior and Exterior Coatings and Finishes, Reinstatement and demands that may be places on Modern Building.</p>

  <div class="thumb" role="img" aria-label="Photo of a two-storey house at dusk" style="left:793px;top:529px"></div>
  <p class="service" style="left:905px;top:526px">B.W.C With our knowledge of Roofing Systems and Metal Cladding we can provide you with Effective Coatings and Applications solutions, often allowing you to repair what you thought you would have to replace.</p>

  <p class="service" style="left:402px;top:645px">B.W.C Offers a full range of Industrial Painting Services and Protective Coatings; and long-term corrosion control, including Protective Coatings to Bridges, Plant, Machinery, and Towers, Pipes Work, Commercial Ovens, Food Processing Equipment, Sprinkler Systems, Air-conditioning Units and Ducting.</p>
  <div class="thumb" role="img" aria-label="Photo of a two-storey house at dusk" style="left:677px;top:651px"></div>

  <p class="service" style="left:793px;top:645px">B.W.C Quality control is crucial to us, and we provide full documentation on all relevant data, such as film thickness and environmental conditions, to assure you we are fully compliant with the manufacturers' application specifications.</p>
  <div class="thumb" role="img" aria-label="Photo of a two-storey house at dusk" style="left:1068px;top:651px"></div>

  <div class="thumb" role="img" aria-label="Photo of a two-storey house at dusk" style="left:401px;top:787px"></div>
  <p class="service" style="left:513px;top:784px">B.W.C has experience in corporate Reimaging and Branding .having worked on a number of large-scale Reimaging and Branding projects, and also offer free colour consultation, Retail, Supermarkets, Shopping Malls, Warehouses.</p>

  <div class="thumb" role="img" aria-label="Photo of a two-storey house at dusk" style="left:793px;top:787px"></div>
  <p class="service" style="left:905px;top:784px">B.W.C team has Extensive Experience in Coating all Surfaces and Substrates whether Concrete Substrates and Metal, Wood, Colour Steel, Fiber Cement, Steel, Textured Concrete, Concrete Flooring.</p>
</div>
</body>
</html>
```